ULMA Networks
Exceeding Your Expectations
Professional
Ged Humbrecht
President
482 Pellow Crescent
Vaughan, Ontario
CANADA, M2J 7K3
ged@ulmanetworks.com
ulmanetworks.com
Open to seeing unique designs.
Must be complimentary to logo color and style.
Logo, QR Code,

```html
<!DOCTYPE html>
<html lang="en">
<head>
<meta charset="utf-8">
<title>Ovarel Networks – Business Card</title>
<link rel="stylesheet" href="https://fonts.googleapis.com/css2?family=Montserrat:wght@400;600;700;800&display=swap">
<style>
  :root {
    --orange: #f39b33;
    --orange-light: #f7ad55;
    --white: #ffffff;
    --paper: #f4f4f4;
    --grey: #9a9a9a;
    --charcoal: #3a3a3a;
    --stage: #e9e9ea;
  }
  * { margin: 0; padding: 0; box-sizing: border-box; }
  html, body {
    width: 1200px; height: 991px; overflow: hidden;
    background: var(--stage);
    font-family: "Montserrat", Arial, sans-serif;
  }
  .stage {
    width: 1200px; height: 991px;
    display: flex; flex-direction: column;
    align-items: center; justify-content: center; gap: 44px;
  }
  .card {
    position: relative;
    width: 760px; height: 434px;
    border-radius: 26px; overflow: hidden;
    box-shadow: 0 6px 18px rgba(0,0,0,.12);
  }
  .card svg.bg { position: absolute; inset: 0; }

  /* front */
  .brand {
    position: absolute; left: 372px; top: 108px;
    display: flex; align-items: center; gap: 12px;
  }
  .brand-mark { width: 22px; height: 22px; background: var(--orange); }
  .brand-name {
    font-weight: 800; font-size: 40px; color: var(--charcoal);
    letter-spacing: .5px; line-height: 1;
  }
  .brand-sub {
    position: absolute; left: 406px; top: 162px;
    font-weight: 800; font-size: 19px; color: var(--charcoal);
  }
  .contact {
    position: absolute; left: 34px; top: 232px;
    list-style: none; color: var(--white);
    font-size: 14px; line-height: 22px; font-weight: 600;
  }
  .contact li { display: flex; align-items: flex-start; gap: 10px; }
  .contact svg { flex: none; margin-top: 3px; }
  .contact .indent { padding-left: 26px; }
  .person {
    position: absolute; right: 40px; bottom: 30px;
    text-align: right; color: var(--white);
  }
  .person-name { font-weight: 700; font-size: 17px; letter-spacing: 1.5px; text-transform: uppercase; }
  .person-role { font-weight: 400; font-size: 14px; letter-spacing: 1.5px; text-transform: uppercase; }

  /* back */
  .back { background: var(--orange); }
  .back-web {
    position: absolute; left: 40px; top: 40px;
    color: var(--white); font-size: 15px; font-weight: 600;
    letter-spacing: 5px; text-transform: uppercase;
  }
  .back-emblem {
    position: absolute; right: 36px; bottom: 70px;
    font-weight: 800; font-size: 118px; line-height: 1;
    color: var(--orange-light);
  }
</style>
</head>
<body>
<main class="stage">

  <section class="card front" aria-label="Card front">
    <svg class="bg" width="760" height="434" viewBox="0 0 760 434">
      <rect width="760" height="434" fill="var(--orange)"/>
      <path d="M0 0 H760 V352 C600 262 330 200 0 196 Z" fill="var(--grey)"/>
      <path d="M0 0 H760 V338 C600 248 330 186 0 182 Z" fill="var(--charcoal)"/>
      <path d="M0 0 H760 V330 C600 236 330 172 0 168 Z" fill="var(--paper)"/>
    </svg>

    <div class="brand">
      <span class="brand-mark"></span>
      <span class="brand-name">OVAREL</span>
    </div>
    <div class="brand-sub">Ovarel Networks Inc.</div>

    <ul class="contact">
      <li>
        <svg width="16" height="16" viewBox="0 0 16 16"><path d="M8 1a5 5 0 0 0-5 5c0 4 5 9 5 9s5-5 5-9a5 5 0 0 0-5-5zm0 7a2 2 0 1 1 0-4 2 2 0 0 1 0 4z" fill="var(--white)"/></svg>
        <span>482 Pellow Crescent</span>
      </li>
      <li class="indent">Vaughan, Ontario</li>
      <li class="indent">CANADA, M2J 7K3</li>
      <li>
        <svg width="16" height="16" viewBox="0 0 16 16"><path d="M4 1l3 3-2 2c1 2 3 4 5 5l2-2 3 3-2 3C7 15 1 9 1 3z" fill="var(--white)"/></svg>
        <span>905-555-0148</span>
      </li>
      <li>
        <svg width="16" height="16" viewBox="0 0 16 16"><rect x="4" y="1" width="8" height="14" rx="1.5" fill="var(--white)"/><rect x="5.5" y="3" width="5" height="8" fill="var(--orange)"/></svg>
        <span>647-555-0192</span>
      </li>
      <li>
        <svg width="16" height="16" viewBox="0 0 16 16"><rect x="1" y="3" width="14" height="10" rx="1" fill="var(--white)"/><path d="M1.5 4l6.5 5 6.5-5" stroke="var(--orange)" stroke-width="1.4" fill="none"/></svg>
        <span>ged@ovarelnetworks.com</span>
      </li>
      <li>
        <svg width="16" height="16" viewBox="0 0 16 16"><circle cx="8" cy="8" r="6.5" stroke="var(--white)" stroke-width="1.5" fill="none"/><path d="M1.5 8h13M8 1.5c-3 3.5-3 9.5 0 13M8 1.5c3 3.5 3 9.5 0 13" stroke="var(--white)" stroke-width="1.2" fill="none"/></svg>
        <span>ovarelnetworks.com</span>
      </li>
    </ul>

    <div class="person">
      <div class="person-name">Ged Humbrecht</div>
      <div class="person-role">President</div>
    </div>
  </section>

  <section class="card back" aria-label="Card back">
    <div class="back-web">www.ovarelnetworks.com</div>
    <div class="back-emblem">OVAREL</div>
  </section>

</main>
</body>
</html>
```